Bref créative
Stationary for Trucking Co
Silver Heron Haulage, Inc.
Professional
Teodoro Villanueva Jr
President
418 W. Marquette St.
Alder Bay, CA 90999
teo@moveshq.example
www.moveshq.example
Looking for a business card that i can ultimately letter press so please keep that in mind. Im looking for Stationary. Letterhead, Fax cover sheet, business cards, e-mail signature. I don't have the office phone and fax yet, but leave room for it. i will have it eventually.
i'd really like a few options for everything.

```html
<!DOCTYPE html>
<html lang="en">
<head>
<meta charset="utf-8">
<title>Silver Heron Haulage – Business Card</title>
<link rel="stylesheet" href="https://fonts.googleapis.com/css2?family=Arimo:wght@400;700&display=swap">
<style>
  :root {
    --backdrop: #e9eaec;
    --card: #ffffff;
    --gold: #c99a1c;
    --gold-deep: #a87a0e;
    --charcoal: #2b2b2d;
    --ink: #3a3a3c;
    --muted: #6a6a6d;
    --rule: #bdbdbd;
  }
  * { box-sizing: border-box; margin: 0; padding: 0; }
  html, body { width: 1200px; height: 838px; overflow: hidden; }
  body {
    background: var(--backdrop);
    font-family: "Arimo", Arial, sans-serif;
    color: var(--ink);
    display: flex;
    align-items: center;
    justify-content: center;
    gap: 40px;
  }
  .card {
    position: relative;
    width: 540px;
    height: 309px;
    background: var(--card);
    box-shadow: 0 10px 26px rgba(0,0,0,.16);
    overflow: hidden;
  }
  /* Front */
  .card-front .brand {
    position: absolute;
    left: 30px;
    top: 88px;
    width: 210px;
    display: flex;
    flex-direction: column;
    align-items: center;
    gap: 14px;
  }
  .brand-dot {
    width: 46px; height: 46px;
    border-radius: 50%;
    background: var(--gold);
  }
  .brand-name {
    color: var(--gold-deep);
    font-weight: 700;
    font-size: 19px;
    letter-spacing: .5px;
    text-transform: uppercase;
    text-align: center;
    line-height: 1.2;
  }
  .divider {
    position: absolute;
    left: 262px;
    top: 70px;
    width: 1px;
    height: 150px;
    background: var(--rule);
  }
  .contact {
    position: absolute;
    left: 280px;
    top: 78px;
    right: 18px;
  }
  .person-name {
    font-size: 21px;
    font-weight: 700;
    color: var(--charcoal);
    white-space: nowrap;
  }
  .person-title {
    font-size: 12px;
    color: var(--muted);
    margin-top: 3px;
  }
  .address {
    font-style: normal;
    font-size: 12px;
    line-height: 1.4;
    color: var(--muted);
    margin-top: 22px;
  }
  .contact-line {
    display: flex;
    align-items: center;
    gap: 6px;
    font-size: 12px;
    color: var(--muted);
    line-height: 1.4;
  }
  .contact-line svg { width: 10px; height: 10px; fill: var(--charcoal); flex: none; }
  .band {
    position: absolute;
    left: 0; bottom: 0;
    width: 540px; height: 44px;
  }
  .website {
    position: absolute;
    right: 26px;
    bottom: 11px;
    color: #fff;
    font-size: 12px;
    letter-spacing: 4px;
  }
  /* Back */
  .card-back .brand-mark {
    position: absolute;
    inset: 0;
    display: flex;
    flex-direction: column;
    align-items: center;
    justify-content: center;
    gap: 16px;
  }
  .card-back .brand-dot { width: 64px; height: 64px; }
  .card-back .brand-name { font-size: 24px; }
</style>
</head>
<body>
  <section class="card card-front" aria-label="Business card front">
    <div class="brand">
      <span class="brand-dot"></span>
      <span class="brand-name">Silver Heron Haulage</span>
    </div>
    <div class="divider"></div>
    <div class="contact">
      <p class="person-name">Teodoro Villanueva Jr</p>
      <p class="person-title">President</p>
      <address class="address">418 W. Marquette St. #120-310<br>Alder Bay, CA 90999</address>
      <p class="contact-line">
        <svg viewBox="0 0 10 10"><rect x="2" y="0" width="6" height="10" rx="1.2"/></svg>
        : 310-555-0148
      </p>
      <p class="contact-line">
        <svg viewBox="0 0 10 10"><path d="M0 2h10v6H0z M0 2l5 3.5L10 2" stroke="#fff" stroke-width=".8"/></svg>
        teo@moveshq.example
      </p>
    </div>
    <svg class="band" viewBox="0 0 540 44" preserveAspectRatio="none" aria-hidden="true">
      <polygon points="0,14 300,14 288,44 0,44" fill="var(--gold)"/>
      <polygon points="300,0 540,0 540,44 282,44" fill="var(--charcoal)"/>
    </svg>
    <p class="website">www.moveshq.example</p>
  </section>

  <section class="card card-back" aria-label="Business card back">
    <div class="brand-mark">
      <span class="brand-dot"></span>
      <span class="brand-name">Silver Heron Haulage</span>
    </div>
  </section>
</body>
</html>
```